Thankyou post card for our customers

we would like to have a design for a post card that we would like to send to our customers once they have hired from us to say thankyou and to offer them a discount on there next hire.

our business is called Wattlebrook Caravan Rentals.
we hire our camper trailers and are based in Australia so alot of our customers go to the outback bush, beach etc with our campers.
the post card dimesions are
Full Bleed Size

213 x 98 mm
2517 x 1158 pixels

Document Trim Size

210 x 95 mm
2481 x 1122 pixels

I want 4 lines for the name and address on the right have side of the post card (like normal post cards have

Requirements
Must have
• we want it to be double sided so a Design on front and back of post card
I have attached our logo and some other things we have used in previous business material up to you if you want to use what I have uploaded

please note the logo with sunset I have attached I do not want the round logo used just wanted to show you how great the sunset looks we have changed our logo to just be the Wattlebrook Caravan Rentals but wouldnt mind if you used a sunset like this on the whole of the card? but not limited to that.

front of card:
our logo on front page (which is just the Wattlebrook Caravan Rentals attachement WCR1)
and our details:
P: 0491 326 715
W: www.wattlebrookcaravanrentals.com.au
E:info@wattlebrookcaravanrentals.com.au

and the following to be on the front of the post card:

Dear Fellow Campers,
We hope you have arrived home safely, and are rested and relaxed from your trip away. It was our pleasure to have you hire one of our campers and would like to thankyou for your support, we trust you enjoyed glamping and would like to think you would hire from us again. to show our appreciation we would like to offer you a 20% discount on any minimum 7 day hire over the next 6 months. we look forward to hearing from you again soon.
sincerely,
Gareth & Colby

offer not valid in peak period or in conjuction with any other offer

Full Bleed Size

213 x 98 mm
2517 x 1158 pixels

Document Trim Size

210 x 95 mm
2481 x 1122 pixels

Back of Card:

I want "Thankyou" written at top and then how ever else you design it

```html
<!DOCTYPE html>
<html lang="en">
<head>
<meta charset="utf-8">
<title>Wattlebrook Caravan Rentals – Thank You Postcard</title>
<link rel="stylesheet" href="https://fonts.googleapis.com/css2?family=Barlow+Semi+Condensed:wght@500;600;700&family=Barlow:wght@800;900&display=swap">
<style>
  :root {
    --stage: #1c0d0d;
    --card: #f4f4f4;
    --card-edge: #e4e4e4;
    --ink: #8a8a8a;
    --ink-soft: #a9a9a9;
    --ink-dark: #1e1e1e;
    --accent: #d8641c;
    --link: #1f8fd0;
    --tread-dark: #9a9a9a;
    --tread-light: #dedede;
    --rule: #c9c9c9;
    --shout: #ffffff;
    --shout-bg: #e9e9e9;
  }
  * { box-sizing: border-box; margin: 0; padding: 0; }
  html, body { width: 1200px; height: 960px; overflow: hidden; }
  body {
    background: var(--stage);
    display: flex; flex-direction: column; align-items: center; justify-content: center;
    gap: 30px;
    font-family: "Barlow Semi Condensed", "Arial Narrow", sans-serif;
  }
  .postcard {
    width: 960px; height: 434px;
    background: var(--card);
    position: relative; overflow: hidden;
    border: 1px solid var(--card-edge);
  }

  /* ---------- Letter side ---------- */
  .tread {
    position: absolute; left: 0; top: 0; bottom: 0; width: 90px;
    background: linear-gradient(90deg, var(--tread-dark), var(--tread-light));
  }
  .brand {
    position: absolute; left: 120px; bottom: 70px;
  }
  .brand-name {
    font-weight: 700; font-size: 40px; line-height: 0.95;
    text-transform: uppercase; color: var(--ink-dark); letter-spacing: 0.5px;
  }
  .brand-web {
    margin-top: 14px;
    font-weight: 600; font-size: 19px; color: var(--link);
  }
  .letter {
    position: absolute; left: 470px; top: 44px; width: 440px;
    text-transform: uppercase; color: var(--ink);
    font-weight: 700; font-size: 17px; line-height: 1.2; letter-spacing: 0.6px;
  }
  .letter p { margin-bottom: 14px; }
  .letter .offer { color: var(--accent); }

  /* ---------- Thank you side ---------- */
  .postcard--back { background: var(--shout-bg); }
  .shout {
    position: absolute; left: 0; right: 0; top: -14px;
    text-align: center;
    font-family: "Barlow", "Arial Black", sans-serif;
    font-weight: 900; font-size: 162px; line-height: 1; letter-spacing: -2px;
    color: var(--shout); white-space: nowrap;
  }
  .address-lines {
    position: absolute; right: 40px; top: 210px; width: 300px;
    list-style: none;
  }
  .address-lines li { height: 38px; border-bottom: 1.5px solid var(--rule); }
  .contact {
    position: absolute; left: 40px; bottom: 32px;
    text-transform: uppercase; color: var(--ink);
    font-weight: 700; font-size: 17px; line-height: 1.25; letter-spacing: 0.6px;
  }
  .contact .fine { font-weight: 500; font-size: 13px; color: var(--ink-soft); margin-top: 2px; }
</style>
</head>
<body>

  <section class="postcard postcard--letter" aria-label="Postcard letter side">
    <div class="tread" role="img" aria-label="Grey tyre tread texture band"></div>
    <div class="brand">
      <div class="brand-name">Wattlebrook<br>Caravan Rentals</div>
      <div class="brand-web">www.wattlebrookcaravanrentals.com.au</div>
    </div>
    <div class="letter">
      <p>Dear Fellow Campers,</p>
      <p>We hope you have arrived home safely, and are rested and relaxed from your trip away.</p>
      <p>It was our pleasure to have you hire one of our campers and would like to thank you for your support, we trust you enjoyed glamping and would like to think you would hire from us again.</p>
      <p>To show our appreciation we would like to offer you a <span class="offer">20% discount*</span> on any minimum 7 day hire over the next 6 months.</p>
      <p>We look forward to hearing from you again soon.</p>
      <p>Sincerely,<br>Gareth &amp; Colby</p>
    </div>
  </section>

  <section class="postcard postcard--back" aria-label="Postcard thank you side">
    <h1 class="shout">THANK YOU</h1>
    <ul class="address-lines" aria-label="Address lines">
      <li></li><li></li><li></li><li></li>
    </ul>
    <div class="contact">
      <div>T 0491 326 715 – www.wattlebrookcaravanrentals.com.au</div>
      <div>info@wattlebrookcaravanrentals.com.au</div>
      <div class="fine">*Offer not valid in peak period or in conjunction with any other offer</div>
    </div>
  </section>

</body>
</html>
```